Redesign of Business Card to look more professional and stand out

Business card design. You can lean more about our company by going to dkrfabworks.example. Raised letters would be nice. Company name & Address
DK&R
418 Wendlow Ridge Drive, Suite 340
Harlow Bend, AL 36910

You can use my name and title: Glenn Harwick
Business Development Manager

Target Market(s)

Heavy Industrial market, i.e. utilities, chemical plants, paper mills, construction companies

Industry/Entity Type

Construction

Contact Information for Business Card

We provide Project Management & Project Support Services

Font styles to use
Serif

Requirements
Must have
• Company name & Address
• DK&R
• 418 Wendlow Ridge Drive, Suite 340
• Harlow Bend, AL 36910
Nice to have
• ideas for the back of the card
Should not have
• no crazy colors. needs to look professional and standout.

```html
<!DOCTYPE html>
<html lang="en">
<head>
<meta charset="utf-8">
<title>DK&amp;R Business Card</title>
<link href="https://fonts.googleapis.com/css2?family=Jost:wght@400;600;700&display=swap" rel="stylesheet">
<style>
  :root {
    --navy: #1d3f7c;
    --navy-light: #2d5591;
    --navy-dark: #17336a;
    --orange: #e57222;
    --orange-light: #ef8a33;
    --white: #ffffff;
    --paper: #f4f5f6;
    --grey-text: #6a6e74;
    --stage: #e4e6e9;
  }
  * { margin: 0; padding: 0; box-sizing: border-box; }
  html, body { width: 1200px; height: 900px; overflow: hidden; }
  body {
    background: var(--stage);
    font-family: "Jost", "Century Gothic", sans-serif;
    position: relative;
  }
  .card {
    position: absolute;
    left: 320px;
    width: 560px;
    height: 320px;
    overflow: hidden;
    box-shadow: 0 8px 24px rgba(0,0,0,0.18);
  }

  /* Back of card */
  .card-back {
    top: 60px;
    background: radial-gradient(ellipse at 50% 60%, var(--navy-light), var(--navy-dark) 80%);
  }
  .card-back .brand {
    position: absolute;
    left: 0; right: 0; top: 92px;
    text-align: center;
    color: var(--white);
  }
  .card-back .brand-name {
    font-weight: 700;
    font-size: 82px;
    line-height: 1;
    letter-spacing: 1px;
  }
  .card-back .brand-url {
    margin-top: 6px;
    font-size: 15px;
    font-weight: 400;
    letter-spacing: 0.3px;
  }
  .card-back .brand-url strong { font-weight: 600; }
  .accent-band {
    position: absolute;
    left: 0; right: 0; bottom: 0;
    height: 26px;
    background: linear-gradient(90deg, var(--orange), var(--orange-light));
  }

  /* Front of card */
  .card-front {
    top: 460px;
    background: linear-gradient(180deg, var(--white), var(--paper));
  }
  .card-front .logo {
    position: absolute;
    right: 44px; top: 34px;
    color: var(--navy);
    font-weight: 700;
    font-size: 62px;
    line-height: 1;
    letter-spacing: 1px;
  }
  .card-front .person {
    position: absolute;
    left: 44px; top: 98px;
  }
  .person-name {
    color: var(--navy);
    font-weight: 600;
    font-size: 19px;
    letter-spacing: 0.5px;
    text-transform: uppercase;
  }
  .person-title {
    color: var(--grey-text);
    font-size: 14px;
    letter-spacing: 0.4px;
  }
  .info-panel {
    position: absolute;
    left: 0; right: 0; top: 176px; bottom: 0;
    background: radial-gradient(ellipse at 60% 40%, var(--navy-light), var(--navy-dark) 85%);
  }
  .info-panel .notch {
    position: absolute;
    left: 118px; top: -1px;
  }
  .address {
    position: absolute;
    right: 30px; top: 14px;
    color: var(--white);
    text-align: right;
    font-size: 13px;
    line-height: 1.35;
  }
  .contacts {
    position: absolute;
    left: 44px; top: 40px;
    list-style: none;
    color: var(--white);
    font-size: 14px;
    line-height: 1;
  }
  .contacts li {
    display: flex;
    align-items: center;
    gap: 9px;
    margin-bottom: 6px;
  }
  .contacts svg { flex: none; }
  .card-front .accent-band { height: 22px; }
</style>
</head>
<body>

<section class="card card-back" aria-label="Back of business card">
  <div class="brand">
    <div class="brand-name">DK&amp;R</div>
    <div class="brand-url">www.<strong>dkrfabworks</strong>.example</div>
  </div>
  <div class="accent-band"></div>
</section>

<section class="card card-front" aria-label="Front of business card">
  <div class="logo">DK&amp;R</div>
  <div class="person">
    <div class="person-name">Glenn Harwick</div>
    <div class="person-title">Business Development Manager</div>
  </div>
  <div class="info-panel">
    <svg class="notch" width="22" height="11" viewBox="0 0 22 11" aria-hidden="true">
      <polygon points="0,0 22,0 11,11" fill="#f6f7f8"/>
    </svg>
    <div class="address">
      418 Wendlow Ridge Drive,<br>
      Suite 340, Harlow Bend,<br>
      AL 36910
    </div>
    <ul class="contacts">
      <li>
        <svg width="16" height="16" viewBox="0 0 16 16" aria-hidden="true">
          <rect width="16" height="16" rx="3" fill="#e57222"/>
          <path d="M5 3.5c.6 0 1.2 1.6 1.2 2 0 .5-.8.8-.8 1.2.4 1.2 1.6 2.4 2.8 2.8.4 0 .7-.8 1.2-.8.4 0 2 .6 2 1.2 0 1-1 1.8-1.8 1.6C6.8 11 5 9.2 4.5 6.3 4.3 5 4.3 3.5 5 3.5z" fill="#fff"/>
        </svg>
        05-555-0142
      </li>
      <li>
        <svg width="16" height="16" viewBox="0 0 16 16" aria-hidden="true">
          <rect width="16" height="16" rx="3" fill="#e57222"/>
          <rect x="3.5" y="5" width="9" height="6.5" fill="none" stroke="#fff" stroke-width="1.2"/>
          <path d="M3.5 5l4.5 3.6L12.5 5" fill="none" stroke="#fff" stroke-width="1.2"/>
        </svg>
        info@dkrfabworks.example
      </li>
      <li>
        <svg width="16" height="16" viewBox="0 0 16 16" aria-hidden="true">
          <rect width="16" height="16" rx="3" fill="#e57222"/>
          <circle cx="8" cy="8" r="4.6" fill="none" stroke="#fff" stroke-width="1.1"/>
          <ellipse cx="8" cy="8" rx="2" ry="4.6" fill="none" stroke="#fff" stroke-width="1"/>
          <path d="M3.4 8h9.2" stroke="#fff" stroke-width="1"/>
        </svg>
        www.dkrfabworks.example
      </li>
    </ul>
    <div class="accent-band"></div>
  </div>
</section>

</body>
</html>
```